Lumora MediSpa - Mailchimp Email

I have a list of prospects that I want to email. I'm using Mailchimp. I would like my template to explain that we are now open and ready for business. We are offering 20% off on all services and special procedure combination deals. I want the design to be a template that I can use the same look and feel for future emails - for information giving, beauty tips. monthly promos, etc.

I don't know much about email campaigns, but I'd like to keep it simple, let the people know we're open for business and try to get them to either respond to the email or call for a free consult.
Updates

Thank you all for your hard work on my project.

Target Market(s)

The list criteria is female, income greater than $50,000, between the age of 30 and 65. The area is affluent - Potomac, Bethesda and Chevy Chase Maryland

Industry/Entity Type

Health And Wellness

Font styles to use
Other font styles liked:
• I'd like to keep the font simple like our logo font - again if possible.

Colors

Designer to choose colors to be used in the design.

Requirements
Must have
• my logo, nice pictures related to the medispa business, location "1 block from Harrowgate Crossing Mall', link to our website
Nice to have
• place to input their info to sign up for future emails - i see this on websites. I don't know if they do this for emails. Mailchimp seems to use them.
• Keep the look and feel of our website if that makes sense - www.lumoramedispa.example.
Should not have
• don't be too busy or too long. Keep it simple if possible.

```html
<!DOCTYPE html>
<html lang="en">
<head>
<meta charset="utf-8">
<title>Lumora MediSpa – Now Open</title>
<link href="https://fonts.googleapis.com/css2?family=Lato:wght@300;400;700&display=swap" rel="stylesheet">
<style>
  :root {
    --green: #5e9a35;
    --ink: #2f2f2f;
    --text: #555555;
    --rule: #c9c9c9;
    --footer: #333333;
    --footer-soft: #cfcfcf;
    --label-bg: rgba(40, 40, 40, 0.78);
    --white: #ffffff;
  }
  * { margin: 0; padding: 0; box-sizing: border-box; }
  html, body { width: 680px; height: 1200px; overflow: hidden; background: var(--white); }
  body { position: relative; font-family: "Lato", Arial, sans-serif; color: var(--ink); }

  .brand {
    position: absolute; top: 26px; left: 0; width: 680px;
    display: flex; justify-content: center; align-items: center; gap: 10px;
  }
  .brand-mark { width: 40px; height: 40px; border-radius: 50%; background: var(--ink); }
  .brand-name { font-size: 28px; font-weight: 700; color: var(--ink); letter-spacing: 0.5px; }

  .hero {
    position: absolute; left: 20px; top: 95px; width: 640px; height: 170px;
    background: linear-gradient(90deg, #d9c7bb 0%, #cfc9c4 45%, #bdbab7 100%);
  }

  .intro {
    position: absolute; left: 50px; top: 278px; width: 580px;
    font-size: 15px; font-weight: 300; line-height: 21px; color: var(--text); text-align: center;
  }

  .rule { position: absolute; left: 20px; width: 640px; border-top: 1px dashed var(--rule); }
  .rule-top { top: 335px; }
  .rule-bottom { top: 457px; }

  .offer { position: absolute; left: 0; top: 348px; width: 680px; text-align: center; }
  .offer-lead { font-size: 17px; font-weight: 400; line-height: 22px; }
  .offer-amount { font-size: 42px; font-weight: 700; color: var(--green); line-height: 50px; }
  .offer-detail { font-size: 17px; font-weight: 400; line-height: 22px; }

  .section-title {
    position: absolute; left: 0; top: 466px; width: 680px; text-align: center;
    font-size: 28px; font-weight: 700; color: var(--ink);
  }

  .service { position: absolute; width: 309px; height: 205px; }
  .service-photo { position: absolute; inset: 0; }
  .service-label {
    position: absolute; left: 0; bottom: 0; padding: 0 10px; height: 24px; line-height: 24px;
    background: var(--label-bg); color: var(--white); font-size: 12.5px; font-weight: 400; text-transform: uppercase;
  }
  .s1 { left: 20px; top: 513px; }
  .s2 { left: 350px; top: 513px; }
  .s3 { left: 20px; top: 739px; }
  .s4 { left: 350px; top: 739px; }
  .s1 .service-photo { background: linear-gradient(135deg, #b89684, #e9ddd6 60%, #cbb6a8); }
  .s2 .service-photo { background: linear-gradient(135deg, #6f7a55, #c98f6c 55%, #8d5a43); }
  .s3 .service-photo { background: linear-gradient(180deg, #c9a38c, #d9c2b3 55%, #b7c3cf); }
  .s4 .service-photo { background: linear-gradient(135deg, #4a4d52, #d6b3a2 55%, #b02a32); }

  .cta {
    position: absolute; left: 253px; top: 975px; width: 174px; height: 33px;
    background: var(--green); color: var(--white); font-size: 12.5px; font-weight: 400;
    display: flex; align-items: center; justify-content: center; text-decoration: none;
  }
  .contact { position: absolute; left: 0; top: 1016px; width: 680px; text-align: center; color: var(--ink); }
  .contact-or { font-size: 12.5px; line-height: 18px; }
  .contact-note { font-size: 12.5px; line-height: 24px; }
  .contact-phone { font-size: 18px; line-height: 28px; }

  .footer { position: absolute; left: 0; top: 1095px; width: 680px; height: 105px; background: var(--footer); color: var(--white); }
  .social-title { position: absolute; left: 20px; top: 15px; font-size: 12px; font-weight: 700; }
  .social { position: absolute; left: 20px; top: 38px; display: flex; gap: 11px; }
  .social-dot { width: 19px; height: 19px; border-radius: 50%; background: var(--green); }
  .site { position: absolute; right: 21px; top: 13px; display: flex; align-items: center; gap: 6px; font-size: 11.5px; font-weight: 700; }
  .footer-phone { position: absolute; right: 21px; top: 37px; font-size: 12.5px; line-height: 16px; }
  .footer-location { position: absolute; right: 21px; top: 56px; font-size: 10.5px; line-height: 14px; color: var(--footer-soft); }
  .copyright { position: absolute; left: 0; top: 75px; width: 680px; text-align: center; font-size: 10px; font-weight: 300; }
</style>
</head>
<body>
  <header class="brand">
    <span class="brand-mark"></span>
    <span class="brand-name">Lumora MediSpa</span>
  </header>

  <div class="hero" role="img" aria-label="Woman relaxing with a clay facial mask during a spa treatment"></div>

  <p class="intro">Our goals are natural beauty and patient satisfaction. We strive to make sure you are happy with your look. We are commited to enhance your natural beauty.</p>

  <div class="rule rule-top"></div>
  <section class="offer">
    <p class="offer-lead">We are now open and offering</p>
    <p class="offer-amount">20% off</p>
    <p class="offer-detail">on all services and special procedure combination deals</p>
  </section>
  <div class="rule rule-bottom"></div>

  <h2 class="section-title">Services</h2>

  <div class="service s1">
    <div class="service-photo" role="img" aria-label="Facial massage treatment"></div>
    <span class="service-label">Facial Aesthetics</span>
  </div>
  <div class="service s2">
    <div class="service-photo" role="img" aria-label="Client with freckled skin for laser treatment"></div>
    <span class="service-label">Laser Skin Treatments</span>
  </div>
  <div class="service s3">
    <div class="service-photo" role="img" aria-label="Hands pinching the waist for body contouring"></div>
    <span class="service-label">Body Contouring / Weight Loss</span>
  </div>
  <div class="service s4">
    <div class="service-photo" role="img" aria-label="Woman with red lips holding a red rose"></div>
    <span class="service-label">Skin Rejuvenation</span>
  </div>

  <a class="cta" href="#">VIEW ALL SERVICES</a>
  <div class="contact">
    <p class="contact-or">or</p>
    <p class="contact-note">Call for a free consultation</p>
    <p class="contact-phone">301.555.0142</p>
  </div>

  <footer class="footer">
    <p class="social-title">Find us at</p>
    <div class="social">
      <span class="social-dot"></span>
      <span class="social-dot"></span>
      <span class="social-dot"></span>
    </div>
    <div class="site">
      <svg width="24" height="24" viewBox="0 0 24 24" fill="none" stroke="#bbbbbb" stroke-width="1.4" aria-hidden="true">
        <circle cx="12" cy="12" r="10"/>
        <ellipse cx="12" cy="12" rx="4.5" ry="10"/>
        <line x1="2" y1="12" x2="22" y2="12"/>
      </svg>
      <span>https://lumoramedispa.example/</span>
    </div>
    <p class="footer-phone">301.555.0142</p>
    <p class="footer-location">1 block from Harrowgate Crossing Mall</p>
    <p class="copyright">Copyright © 2019 Lumora Medi Spa. All Rights Reserved.</p>
  </footer>
</body>
</html>
```